Local fast-growing company in the service sector

We are looking for a modern business card design, which should also appear on our letterheads

Target Market(s)

Private and industrial sectors

Contact Information for Business Card

Vorname Name
Lindkofer Str. 18
71468 Remsbühl
Tel.: 07163-418259-0
Name@kovaltec-pbz.de

Colors
9d9d9d
919191
aaaaaa

Requirements
Must have
• The logo (file) in silver

```html
<!DOCTYPE html>
<html lang="de">
<head>
<meta charset="utf-8">
<title>PBZ Visitenkarte</title>
<link rel="stylesheet" href="https://fonts.googleapis.com/css2?family=Lato:wght@400;700;900&display=swap">
<style>
  :root {
    --stage: #2a2a2a;
    --card-light: #fbfbfb;
    --card-mid: #ececec;
    --card-shade: #dcdcdc;
    --silver: #9d9d9d;
    --silver-dark: #919191;
    --silver-light: #aaaaaa;
    --ink: #555555;
    --ink-soft: #6a6a6a;
    --rule: #3c3c3c;
  }
  * { margin: 0; padding: 0; box-sizing: border-box; }
  html, body {
    width: 1200px;
    height: 997px;
    overflow: hidden;
    background: var(--stage);
    font-family: "Lato", Arial, sans-serif;
  }
  .business-card {
    position: absolute;
    left: 180px;
    top: 256px;
    width: 840px;
    height: 484px;
    overflow: hidden;
  }
  .card-texture {
    position: absolute;
    inset: 0;
    background: linear-gradient(135deg, var(--card-light) 0%, var(--card-mid) 45%, var(--card-light) 70%, var(--card-shade) 100%);
  }
  .brand {
    position: absolute;
    top: 78px;
    left: 0;
    right: 0;
    display: flex;
    justify-content: center;
    align-items: center;
    gap: 18px;
  }
  .brand-square {
    width: 58px;
    height: 58px;
    background: var(--silver);
  }
  .brand-name {
    font-weight: 900;
    font-size: 84px;
    line-height: 1;
    letter-spacing: 2px;
    color: var(--silver-dark);
  }
  .person {
    position: absolute;
    right: 440px;
    top: 300px;
    text-align: right;
  }
  .person-name {
    font-weight: 700;
    font-size: 22px;
    color: var(--ink);
  }
  .person-company {
    font-size: 16px;
    color: var(--ink-soft);
    margin-top: 4px;
  }
  .divider {
    position: absolute;
    left: 418px;
    top: 232px;
    width: 2px;
    height: 130px;
    background: var(--rule);
  }
  .contact {
    position: absolute;
    left: 446px;
    top: 220px;
    list-style: none;
  }
  .contact-line {
    display: flex;
    align-items: center;
    gap: 12px;
    font-size: 17px;
    color: var(--ink);
    height: 32px;
  }
  .contact-icon {
    width: 22px;
    height: 22px;
    border-radius: 50%;
    background: var(--silver-light);
    display: flex;
    align-items: center;
    justify-content: center;
  }
  .address {
    position: absolute;
    left: 446px;
    top: 300px;
    font-style: normal;
    font-weight: 700;
    font-size: 18px;
    line-height: 30px;
    color: var(--ink);
  }
</style>
</head>
<body>
  <section class="business-card">
    <div class="card-texture" role="img" aria-label="Helles, facettiertes Polygonmuster in Silbergrau"></div>

    <header class="brand">
      <span class="brand-square"></span>
      <span class="brand-name">PBZ</span>
    </header>

    <div class="person">
      <p class="person-name">Miriam Hallberg</p>
      <p class="person-company">Norvik Partners</p>
    </div>

    <span class="divider"></span>

    <ul class="contact">
      <li class="contact-line">
        <span class="contact-icon">
          <svg width="12" height="12" viewBox="0 0 12 12"><path d="M2 1h2l1 3-1.5 1a6 6 0 0 0 3.5 3.5L8 7l3 1v2a1 1 0 0 1-1 1A9 9 0 0 1 1 2a1 1 0 0 1 1-1z" fill="#fff"/></svg>
        </span>
        07163-418259-0
      </li>
      <li class="contact-line">
        <span class="contact-icon">
          <svg width="12" height="10" viewBox="0 0 12 10"><rect x="0.5" y="0.5" width="11" height="9" fill="#fff"/><path d="M0.5 0.8 6 5.5 11.5 0.8" stroke="#aaaaaa" fill="none"/></svg>
        </span>
        mhallberg@kovaltec-pbz.de
      </li>
    </ul>

    <address class="address">
      Lindkofer Str. 18<br>
      71468 Remsbühl
    </address>
  </section>
</body>
</html>
```